Luxury supplement label and packaging design

I want to bring to fruition my vision for a line of supplements my business will be coming out with. Our place in the fitness space will cater to high end/ luxury good buyers. We have a Greek theme (Sable Crest) and I would like to incorporate a Greek key pattern along the border or somewhere. I have a logo made, as well as other design concepts o could show you I have an idea for. Please contact me if you decide to take this job. Some design inspiration include brands such as Morvane, Pellet, Durand, Halvorn, and Vitrashore. I have a name for the product/s I want labels created for.

Target Market(s)

High end/ luxury buyers. Men (age 27-39) Women (21-45). Fitness activists who enjoy luxury lifestyle brands.

Industry/Entity Type

Supplement

Font styles to use
Other font styles liked:
• CSL Greek Medium, Trajan Pro

Colors
fbee3f

Requirements
Must have
• Black, white, gold color combo. Greek Key pattern on top, bottom or both borders. Logo. Name of product available upon request.
• Name of product: THE CROWN
• Size: image attached
• Logo: Image attached
• Product description: image attached
Nice to have
• Ask for nutrition facts. Statements that are creative and appealing on side of label, description. Greek Font, uppercase. CSL Greek Medium

```html
<!DOCTYPE html>
<html lang="en">
<head>
<meta charset="utf-8">
<title>Sable Crest – The Crown Premium Pre Workout Label</title>
<link rel="stylesheet" href="https://fonts.googleapis.com/css2?family=Cinzel:wght@400;600;700;800&family=Open+Sans:ital,wght@0,700;0,800;1,500&display=swap">
<style>
  :root {
    --canvas: #ffffff;
    --label-black: #0c0c0c;
    --label-dot: #1d1d1d;
    --gold: #d4a62a;
    --gold-light: #fbee3f;
    --gold-deep: #8a6a12;
    --silver: #e6e6e6;
    --silver-dark: #8c8c8c;
    --text-light: #e8e8e8;
  }
  * { margin: 0; padding: 0; box-sizing: border-box; }
  html, body { width: 1200px; height: 1037px; overflow: hidden; background: var(--canvas); }
  .canvas { position: relative; width: 1200px; height: 1037px; }

  .label {
    position: absolute; left: 210px; top: 230px; width: 780px; height: 580px;
    background-color: var(--label-black);
    background-image: radial-gradient(var(--label-dot) 1.2px, transparent 1.4px);
    background-size: 6px 6px;
    overflow: hidden;
  }
  .label__rim {
    position: absolute; left: 0; right: 0; top: 14px; height: 3px;
    background: linear-gradient(90deg, var(--silver-dark), var(--silver), var(--silver-dark));
  }

  .brand { position: absolute; left: 0; right: 0; top: 70px; text-align: center; }
  .brand__mark {
    display: inline-flex; align-items: center; gap: 14px;
    font-family: "Cinzel", serif; font-weight: 600; font-size: 30px;
    letter-spacing: 3px; color: var(--gold); text-transform: uppercase;
  }
  .brand__dot { width: 18px; height: 18px; border-radius: 50%; background: var(--gold); }
  .brand__tagline {
    margin-top: 10px; font-family: "Cinzel", serif; font-weight: 400;
    font-size: 14px; letter-spacing: 2px; color: var(--gold);
  }

  .product { position: absolute; left: 0; right: 0; top: 196px; text-align: center; }
  .product__name {
    font-family: "Cinzel", serif; font-weight: 800; font-size: 76px; line-height: 1;
    letter-spacing: 1px;
    background: linear-gradient(180deg, var(--gold-light) 0%, var(--silver) 45%, var(--silver-dark) 60%, var(--gold) 100%);
    -webkit-background-clip: text; background-clip: text; color: transparent;
  }
  .product__type {
    margin-top: 16px; font-family: "Cinzel", serif; font-weight: 700;
    font-size: 26px; letter-spacing: 1.5px; color: var(--text-light);
  }

  .servings {
    position: absolute; left: 100px; top: 428px; width: 86px; height: 78px;
    border-radius: 8px; text-align: center;
    background: linear-gradient(160deg, var(--gold-light), var(--gold) 55%, var(--gold-deep));
    font-family: "Open Sans", sans-serif; color: var(--label-black);
  }
  .servings__count { display: block; font-weight: 800; font-size: 34px; line-height: 44px; }
  .servings__unit { display: block; font-weight: 700; font-size: 12px; }

  .facts {
    position: absolute; left: 226px; top: 475px; display: flex; gap: 18px;
    font-family: "Open Sans", sans-serif; font-style: italic; font-weight: 500; font-size: 15px;
  }
  .facts__kind { color: var(--gold); }
  .facts__weight { color: var(--text-light); }

  .key-band {
    position: absolute; left: 0; right: 0; top: 516px; height: 30px;
    background: linear-gradient(180deg, var(--gold-deep), var(--gold-light) 50%, var(--gold-deep));
  }
</style>
</head>
<body>
<main class="canvas">
  <section class="label">
    <div class="label__rim"></div>

    <header class="brand">
      <div class="brand__mark"><span class="brand__dot"></span>Sable Crest</div>
      <p class="brand__tagline">HEALTH AND FITNESS</p>
    </header>

    <div class="product">
      <h1 class="product__name">THE CROWN</h1>
      <p class="product__type">PREMIUM PRE WORKOUT</p>
    </div>

    <div class="servings">
      <span class="servings__count">30</span>
      <span class="servings__unit">Servings</span>
    </div>

    <p class="facts">
      <span class="facts__kind">Dietary Supplement</span>
      <span class="facts__weight">Net Weight 1500g</span>
    </p>

    <div class="key-band" role="img" aria-label="Gold Greek key meander border band"></div>
  </section>
</main>
</body>
</html>
```